Redesign of Brightvale.com website

Our website was initially developed 6+ years ago and has been maintained by several different designers. As a result, it is overly complex, inconsistent format/layout and the content is not well structured/easy to navigate

We need the site redeveloped with a more modern look and feel, simpler content structure and ability to implement new/improved tools, such as: Dynamic Forms, Sales Funnels, Landing Pages, improved metadata of our pages and posts, improved SEO/Page ranking, etc.

We currently use SalesForce CRM, Constant Contact for marketing automation and SmartSheet forms. We are investigating Zapier for workflow integration which could extend to our website.

Our current website is developed in WordPress, ideally we will stick with this platform, but we’re happy to consider other CMS' if strongly recommended. We may decide to remove/consolidate some of the pages and/or content as part of this re-design.

We don't want to rebrand (ie change corporate logo, colours scheme etc) as part of this website redevelopment and it is critical that we don't lose our current Page Ranking, SEO rankings, backlink benefits, etc as part of this redevelopment.

Sites we like the feel/design of are: plorvista.com, quindlefax.com and tovalip.com

Target Market(s)

Corporate, Enterprise and Government B2B clients.

Coding

Coded - Design and coding required

Number of Pages Required

5+ page

Font styles to use
Sans Serif

Colors
ffffff
ec1f27

Requirements
Must have
• Must retain the majority of content on our existing website (although we may re-write some of it as part of this redesign process).
Nice to have
• See above "Project Description"
Should not have

```html
<!DOCTYPE html>
<html lang="en">
<head>
<meta charset="utf-8">
<title>Brightvale – Your Trusted Advisor</title>
<link href="https://fonts.googleapis.com/css2?family=Quicksand:wght@400;500;600;700&family=Poppins:wght@400;500;600;700;800&display=swap" rel="stylesheet">
<style>
:root{
  --red:#ec1f27;
  --red-deep:#c21219;
  --white:#ffffff;
  --ink:#111111;
  --navy:#07172a;
  --panel:#121a27;
  --black:#000000;
  --cyan:#1ab0ef;
  --blue-num:#1aa6e8;
  --grey-quote:#a9a9a9;
}
*{margin:0;padding:0;box-sizing:border-box}
html,body{width:1200px;height:2949px;overflow:hidden;background:var(--white)}
body{position:relative;font-family:"Quicksand",sans-serif;color:var(--ink)}
.abs{position:absolute}

/* header */
.site-header{position:absolute;left:0;top:0;width:1200px;height:135px;background:linear-gradient(90deg,#eeeeee 0%,#f7f7f7 30%,#ffffff 50%)}
.brand{position:absolute;display:flex;align-items:center;gap:8px;font-family:"Quicksand",sans-serif;font-weight:600;color:var(--red)}
.brand-mark{width:26px;height:26px;border-radius:50%;background:var(--red)}
.brand-name{font-size:34px;line-height:1}
.brand-tag{position:absolute;font-size:10px;color:#999;font-weight:500}
.main-nav a{position:absolute;top:93px;font-size:15px;letter-spacing:1.2px;color:#111;text-decoration:none;font-weight:500;transform:translateX(-50%)}
.main-nav a.active::after{content:"";position:absolute;left:0;right:0;bottom:-6px;height:2px;background:var(--red)}

/* hero */
.hero{position:absolute;left:0;top:135px;width:1200px;height:432px;overflow:hidden}
.hero-photo{position:absolute;inset:0;background:linear-gradient(90deg,#1d3a66 0%,#2b4c7c 25%,#8c8a96 45%,#e6e1e6 62%,#f1ecef 80%,#d8d4da 100%)}
.hero-title{position:absolute;left:665px;top:148px;font-size:45px;line-height:54px;font-weight:500;color:#111;letter-spacing:.5px}
.hero-sub{position:absolute;left:667px;top:251px;font-size:16px;line-height:20px;color:#444}

/* intro */
.intro-title{position:absolute;left:0;width:1130px;top:598px;text-align:center;font-size:34px;font-weight:500}
.intro-quote{position:absolute;left:0;width:1130px;top:647px;text-align:center;font-size:18px;font-style:italic}
.intro-body{position:absolute;left:70px;width:1052px;font-size:13.2px;line-height:20.5px;font-weight:500}

/* services */
.services{position:absolute;left:0;top:935px;width:1200px;height:488px;background:radial-gradient(ellipse at 60% 40%,#0e2a44 0%,#081b30 45%,#050f1c 100%);color:var(--white)}
.services-heading{position:absolute;left:161px;top:38px;font-size:52px;font-weight:500}
.btn-cyan{position:absolute;left:169px;top:105px;width:179px;height:32px;background:var(--cyan);color:#0a1a2a;font-size:16px;font-weight:600;text-align:center;line-height:32px;letter-spacing:.5px}
.services-intro{position:absolute;left:492px;top:54px;width:540px;font-size:16px;line-height:19px;font-weight:500}
.service-col{position:absolute;top:203px;width:300px}
.service-col h3{font-size:21px;font-weight:700;margin-bottom:6px}
.service-col li{list-style:none;font-size:14px;line-height:23.2px;font-weight:500}
.btn-red{display:block;margin-top:12px;width:123px;height:31px;background:var(--red-deep);color:var(--white);font-size:14px;font-weight:700;text-align:center;line-height:31px}

/* facts */
.facts{position:absolute;left:0;top:1423px;width:1163px;height:293px;background:var(--black);color:var(--white);box-shadow:3px 4px 6px rgba(0,0,0,.35);text-align:center}
.facts h2{position:absolute;left:0;width:1190px;top:35px;font-size:52px;font-weight:700;letter-spacing:6px}
.facts p{position:absolute;left:0;width:1140px;top:92px;font-size:15px;line-height:23px;font-weight:700}
.fact{position:absolute;top:198px;width:240px;transform:translateX(-50%)}
.fact b{display:block;color:var(--blue-num);font-size:20px;font-weight:700}
.fact span{display:block;font-size:21px;font-weight:500;margin-top:4px}

/* testimonial */
.portrait{position:absolute;left:135px;top:1760px;width:340px;height:466px;background:linear-gradient(180deg,#dfe3e9 0%,#5c6f8c 45%,#34486a 100%);border-radius:120px 120px 0 0}
.quote-mark{position:absolute;left:420px;top:1690px;font-family:"Poppins",sans-serif;font-size:190px;line-height:1;color:var(--grey-quote);font-weight:800}
.testi-title{position:absolute;left:510px;top:1790px;font-size:42px;line-height:48px;font-weight:500}
.testi-body{position:absolute;left:515px;top:1908px;width:500px;font-size:15.5px;line-height:20.5px;font-weight:500;color:#222}
.testi-name{position:absolute;left:515px;top:2011px;font-size:17px;font-weight:700}
.testi-role{position:absolute;left:515px;top:2038px;font-size:17px;font-weight:500}
.arrow-btn{position:absolute;top:2095px;width:38px;height:38px;border-radius:50%;background:#d3141c}

/* contact */
.red-band{position:absolute;left:0;top:2377px;width:1200px;height:271px;background:var(--red-deep)}
.contact-panel{position:absolute;left:161px;top:2226px;width:908px;height:354px;background:var(--panel);color:var(--white);font-family:"Poppins",sans-serif}
.contact-kicker{position:absolute;left:39px;top:33px;font-size:9px;font-weight:700;letter-spacing:.3px}
.contact-rule{position:absolute;left:39px;top:57px;width:36px;height:2px;background:var(--red)}
.contact-heading{position:absolute;left:39px;top:66px;font-size:31px;line-height:36px;font-weight:800}
.contact-text{position:absolute;left:39px;top:145px;font-size:11.5px}
.contact-address{position:absolute;left:39px;top:280px;font-size:11.5px;line-height:15px}
.socials{position:absolute;left:328px;top:289px;display:flex;gap:8px}
.socials i{width:17px;height:17px;border-radius:50%;background:var(--white)}
.field-label{position:absolute;font-size:9px}
.field{position:absolute;background:var(--white);border:1px solid #cfcfcf}
.btn-send{position:absolute;left:464px;top:281px;width:114px;height:29px;background:var(--red);font-size:10px;font-weight:700;text-align:center;line-height:29px}

/* footer */
.site-footer{position:absolute;left:0;top:2648px;width:1200px;height:301px;background:var(--black);color:var(--white);font-family:"Poppins",sans-serif}
.foot-links a{position:absolute;font-size:10px;font-weight:600;color:var(--white);text-decoration:none}
.foot-divider{position:absolute;top:24px;width:1px;height:194px;background:#777}
.foot-contact{position:absolute;right:104px;top:36px;text-align:right;font-size:15px;line-height:20.5px}
.copyright{position:absolute;left:95px;top:260px;font-size:13px}
</style>
</head>
<body>

<header class="site-header">
  <div class="brand" style="left:478px;top:24px">
    <span class="brand-mark"></span><span class="brand-name">brightvale</span>
  </div>
  <span class="brand-tag" style="left:598px;top:56px">your trusted advisor</span>
  <nav class="main-nav">
    <a href="#" class="active" style="left:211px">HOME</a>
    <a href="#" style="left:313px">ABOUT</a>
    <a href="#" style="left:430px">SERVICES</a>
    <a href="#" style="left:552px">CLIENTS</a>
    <a href="#" style="left:684px">RESOURCES</a>
    <a href="#" style="left:805px">BLOG</a>
    <a href="#" style="left:929px">CONTACT US</a>
  </nav>
</header>

<section class="hero">
  <div class="hero-photo" role="img" aria-label="Businessman in a blue suit using a smartphone against a soft blurred office background"></div>
  <svg class="abs" style="left:0;top:0" width="1200" height="432" viewBox="0 0 1200 432">
    <polygon points="700,132 941,27 1045,268 804,373" fill="none" stroke="#ffffff" stroke-width="2.5"/>
  </svg>
  <h1 class="hero-title">LET’S BUILD<br>SOMETHING.</h1>
  <p class="hero-sub">We work with the most innovative solution on<br>the market to help you get the best result</p>
</section>

<section class="intro">
  <h2 class="intro-title" style="left:0;width:1130px">How To Ensure Your Business Is 100% Safe?</h2>
  <p class="intro-quote">“Your business is only as strong as its weakest link.”</p>
  <p class="intro-body" style="top:697px">As an executive in any business, it is understandable that you want to ensure it is 100% safe, because your business is only as strong as its weakest link.</p>
  <p class="intro-body" style="top:739px">You know that if you have a disastrous incident it will cause irreversible damage to your company’s good name, your shareholders, board of directors and industry regulators. It will also cause severe legal ramifications. Sure, you can insure the physical assets of your business with an insurance policy, but it’s not the desks, chairs and IT infrastructure that keeps you in business, it’s your business processes and your staff.V</p>
  <p class="intro-body" style="top:819px">There are strong commercial advantages to having a business continuity process in place, including boosting your brand perception, marketability and adherence to regulatory requirements.</p>
  <p class="intro-body" style="top:879px">We help you make sure that an incident won’t affect in your business by providing you with the industry skills, expertise and knowledge to ensure that your business goes beyond mere compliance to business continuity and recovery standards, through to a workable plan.</p>
</section>

<section class="services">
  <h2 class="services-heading">Services</h2>
  <a class="btn-cyan">VIEW MORE</a>
  <div class="services-intro">
    <p>Our services are tailored to suit your business: regardless of size, industry and demographic.</p>
    <p style="margin-top:18px">We deliver consistent results, whether we’re working with the largest brand names around the world, or the smallest local company.</p>
  </div>
  <div class="service-col" style="left:161px">
    <h3>Software Solutions</h3>
    <ul><li>- Digital Information Security Policy</li><li>- Information Security Management</li><li>- Cyber Security Awareness Training</li><li>- Security Review and Assessment</li><li>- Security Risk Management</li><li>- Vulnerability Identification &amp; Testing</li><li>- Penetration Testing</li><li>- Network Traffic Analysis</li></ul>
    <a class="btn-red">LEARN MORE</a>
  </div>
  <div class="service-col" style="left:483px">
    <h3>Data Management</h3>
    <ul><li>- Digital Information Security Policy</li><li>- Information Security Management</li><li>- Cyber Security Awareness Training</li><li>- Security Review and Assessment</li><li>- Security Risk Management</li><li>- Vulnerability Identification &amp; Testing</li><li>- Penetration Testing</li><li>- Network Traffic Analysis</li></ul>
    <a class="btn-red">LEARN MORE</a>
  </div>
  <div class="service-col" style="left:810px">
    <h3>Security Management</h3>
    <ul><li>- Digital Information Security Policy</li><li>- Information Security Management</li><li>- Cyber Security Awareness Training</li><li>- Security Review and Assessment</li><li>- Security Risk Management</li><li>- Vulnerability Identification &amp; Testing</li><li>- Penetration Testing</li><li>- Network Traffic Analysis</li></ul>
    <a class="btn-red">LEARN MORE</a>
  </div>
</section>

<section class="facts">
  <h2>FUN FACTS</h2>
  <p>Over the years we have done many things that we are proud of. This motivates us to continue<br>looking for new challenges in order to improve our services</p>
  <div class="fact" style="left:203px"><b>488</b><span>Great Projects</span></div>
  <div class="fact" style="left:441px"><b>228</b><span>Innovations</span></div>
  <div class="fact" style="left:707px"><b>903</b><span>Cups of Coffee</span></div>
  <div class="fact" style="left:968px"><b>888</b><span>Happy Customer</span></div>
</section>

<section class="testimonial">
  <div class="portrait" role="img" aria-label="Portrait of a business partner in a navy suit with arms crossed"></div>
  <div class="quote-mark">“</div>
  <h2 class="testi-title">Real Testimonials<br>from our partners</h2>
  <p class="testi-body">It was good to work with you. There are very few true professional organizations such as yours, in this industry. I wish you all the best and I would indeed enjoy working with you again.</p>
  <p class="testi-name">Daniel Harrow</p>
  <p class="testi-role">Head of Infrastructure Services - Norvex Systems</p>
  <span class="arrow-btn" style="left:978px"><svg width="38" height="38" viewBox="0 0 38 38"><polyline points="22,12 15,19 22,26" fill="none" stroke="#fff" stroke-width="2.5"/></svg></span>
  <span class="arrow-btn" style="left:1024px"><svg width="38" height="38" viewBox="0 0 38 38"><polyline points="16,12 23,19 16,26" fill="none" stroke="#fff" stroke-width="2.5"/></svg></span>
</section>

<div class="red-band"></div>
<section class="contact-panel">
  <p class="contact-kicker">CONTACT US TODAY</p>
  <span class="contact-rule"></span>
  <h2 class="contact-heading">We want to help you<br>transform your business.</h2>
  <p class="contact-text">Call us at +612 5550 1420 today. Fill out our contact form, or visit us;</p>
  <p class="contact-address">Level 14, Harbour Point,<br>88 Carrow Street,<br>Sydney NSW 2000 Australia</p>
  <div class="socials"><i></i><i></i><i></i><i></i></div>
  <span class="field-label" style="left:464px;top:39px">Your Name</span>
  <span class="field-label" style="left:670px;top:39px">Company</span>
  <span class="field" style="left:464px;top:57px;width:196px;height:33px"></span>
  <span class="field" style="left:670px;top:57px;width:197px;height:33px"></span>
  <span class="field-label" style="left:464px;top:101px">Email Address</span>
  <span class="field-label" style="left:670px;top:101px">Phone</span>
  <span class="field" style="left:464px;top:119px;width:196px;height:33px"></span>
  <span class="field" style="left:670px;top:119px;width:197px;height:33px"></span>
  <span class="field-label" style="left:464px;top:164px">Email Address</span>
  <span class="field" style="left:464px;top:181px;width:403px;height:86px"></span>
  <a class="btn-send">GET IN TOUCH</a>
</section>

<footer class="site-footer">
  <nav class="foot-links">
    <a style="left:100px;top:35px">HOME</a>
    <a style="left:100px;top:76px">ABOUT</a>
    <a style="left:100px;top:117px">SERVICES</a>
    <a style="left:100px;top:158px">CLIENTS</a>
    <a style="left:227px;top:35px">TESTIMONIALS</a>
    <a style="left:227px;top:76px">MEET THE TEAM</a>
    <a style="left:227px;top:117px">PARTNERS</a>
    <a style="left:227px;top:158px">FAQ</a>
    <a style="left:393px;top:35px">RESOURCES</a>
    <a style="left:393px;top:76px">BLOG</a>
    <a style="left:393px;top:117px">CONTACT</a>
  </nav>
  <span class="foot-divider" style="left:181px"></span>
  <span class="foot-divider" style="left:347px"></span>
  <div class="foot-contact">
    <p>+612 5550 1420</p>
    <p style="margin-top:12px">Level 14, Harbour Point,<br>88 Carrow Street,<br>Sydney NSW 2000 Australia</p>
  </div>
  <div class="brand" style="left:895px;top:210px">
    <span class="brand-mark"></span><span class="brand-name" style="font-size:32px">brightvale</span>
  </div>
  <span class="brand-tag" style="left:1006px;top:242px;color:#ccc">your trusted advisor</span>
  <p class="copyright">© Copyright 2021. BRIGHTVALE. All Rights Reseved.</p>
</footer>

</body>
</html>
```